Beautiful & Elegant Digital Brochure Needed For Luxury Real Estate Development

Hello,

Our company is seeking a beautiful design for our real estate development that is currently being launched.

About The Project:
Development Name - Willow Crest Estate
Location - Charleston, S.C.
Low-Country Southern Style Architecture
Google "low-country" Charleston, SC to get an idea of the unique culture of the city
Google "willow crest tree" Charleston, SC to understand the branding

Other Digital Brochures that we love

http://www.fernvalehotels.example/cedarhollow/wp-content/uploads/sites/6/2014/08/adventures-brochure.pdf

Why we like it... We love the classy feeling the brochure portrays by using unique fonts and backgrounds (burlap textures). We also love the images that represent a "low-country" vibe.

Requirements:
1. We will be providing all of the content (attached)

2. Please use plenty of southern low-country stock images from PixelVaultStock (we have a subscription so just use the watermarked images unless you have full permissions)

3. Do not copy the Cedar Hollow brochure - create a unique vision that fits in to the low-country and southern vibe

4. Attached is our logos

The font we like to use is - Caslon Antique / italic
Thank you!

Project Deadline Extended Reason: We've added more design information and we need to get more designers to participate. Added Monday, May 30, 2016

Target Market(s)

High net worth individuals - each homesite will be over 6 million dollars USD

Industry/Entity Type

Real Estate Development

Font styles to use
Script
Other font styles liked:
• Caslon Antique & Italic

Colors
abd036
00a990
acd036
9bcb3c
33b8a4
86cfc6
cfeae6

Requirements
Must have
• low country feeling
Nice to have
• burlap, wood backgrounds
Should not have
• Should NOT be corporate. This brochure is for multi-millionaire home buyers and investors. They are seeking simple, beautiful, quiet, serene, and southern lifestyles on the Intracoastal waterway on Marley Isle, Charleston, South Carolina.

```html
<!DOCTYPE html>
<html lang="en">
<head>
<meta charset="utf-8">
<title>Willow Crest Estate – Brochure</title>
<link rel="stylesheet" href="https://fonts.googleapis.com/css2?family=Cinzel:wght@600;700&family=Great+Vibes&family=Tinos&family=Lato:wght@400&display=swap">
<style>
  :root {
    --lime: #acd036;
    --green: #9bcb3c;
    --teal: #00a990;
    --teal-mid: #33b8a4;
    --teal-soft: #86cfc6;
    --mint: #cfeae6;
    --gold-light: #f3dc8c;
    --gold: #c9a449;
    --gold-dark: #8a6a22;
    --burlap-light: #b99263;
    --burlap-dark: #84602f;
    --ink: #2a1c0e;
    --footer: #111111;
    --stage: #6b5239;
  }
  * { box-sizing: border-box; margin: 0; padding: 0; }
  html, body { width: 1200px; height: 907px; overflow: hidden; }
  body { background: var(--stage); position: relative; font-family: "Tinos", serif; }

  .page {
    position: absolute; top: 70px; width: 548px; height: 764px;
    overflow: hidden; background: #fff;
    box-shadow: 0 4px 14px rgba(0,0,0,.45);
  }
  .page--cover { left: 48px; }
  .page--inside { left: 608px; }
  .page__art { position: absolute; inset: 0; }

  .brand {
    position: absolute; top: 24px; left: 0; width: 100%; text-align: center;
    font-family: "Cinzel", serif; font-weight: 600; color: var(--gold);
  }
  .brand__name { font-size: 46px; line-height: 1; letter-spacing: 1px; }
  .brand__sub { font-size: 22px; line-height: 1; letter-spacing: 9px; margin-top: 12px; }

  .welcome {
    position: absolute; top: 574px; left: 0; width: 100%; text-align: center;
    font-family: "Cinzel", serif; font-weight: 700; font-size: 44px; line-height: 1;
    color: #fff; letter-spacing: 1px;
    text-shadow: 0 2px 4px rgba(0,0,0,.4);
  }

  .gold-banner {
    position: absolute; border-radius: 6px;
    background: linear-gradient(180deg, var(--gold-light) 0%, var(--gold) 45%, #b08a35 70%, var(--gold-light) 100%);
    border: 2px solid var(--gold-dark);
    box-shadow: 0 2px 5px rgba(0,0,0,.35);
    font-family: "Great Vibes", cursive; color: var(--ink);
    display: flex; align-items: center; justify-content: center; text-align: center;
    white-space: nowrap;
  }
  .gold-banner--community { left: 22px; top: 622px; width: 496px; height: 46px; font-size: 30px; }
  .gold-banner--about { left: 170px; top: 12px; width: 198px; height: 34px; font-size: 24px; border-radius: 17px; }
  .gold-banner--legend { left: 26px; top: 284px; width: 200px; height: 26px; font-size: 15px; justify-content: flex-start; padding-left: 6px; }
  .gold-banner--outdoor { left: 285px; top: 268px; width: 213px; height: 44px; font-size: 17px; line-height: 1.05; white-space: normal; justify-content: flex-start; padding-left: 8px; text-align: left; }

  .footer {
    position: absolute; left: 0; bottom: 0; width: 100%; height: 59px;
    background: var(--footer); color: #fff;
    font-family: "Lato", sans-serif; font-size: 15px;
    display: flex; justify-content: space-between; align-items: center;
    padding: 0 34px 6px;
  }

  .copy { position: absolute; color: var(--ink); text-align: justify; }
  .copy--intro { left: 32px; top: 56px; width: 486px; font-size: 10px; line-height: 1.4; color: #222; }
  .copy--legend { left: 28px; top: 322px; width: 198px; font-size: 8px; line-height: 1.32; text-align: center; }
  .copy--outdoor { left: 285px; top: 322px; width: 215px; font-size: 8px; line-height: 1.32; }
  .copy--inland { left: 30px; top: 546px; width: 490px; font-size: 8px; line-height: 1.3; }
</style>
</head>
<body>

<section class="page page--cover">
  <svg class="page__art" viewBox="0 0 548 764" width="548" height="764" aria-hidden="true">
    <defs>
      <linearGradient id="burlap-cover" x1="0" y1="0" x2="0" y2="1">
        <stop offset="0" stop-color="var(--burlap-light)"/>
        <stop offset="1" stop-color="var(--burlap-dark)"/>
      </linearGradient>
      <linearGradient id="paper" x1="0" y1="0" x2="0" y2="1">
        <stop offset="0" stop-color="#f7f7f7"/>
        <stop offset="1" stop-color="#e6e6e6"/>
      </linearGradient>
      <radialGradient id="forest" cx="0.55" cy="0.45" r="0.7">
        <stop offset="0" stop-color="#eef2de"/>
        <stop offset="0.35" stop-color="#a9c47a"/>
        <stop offset="0.75" stop-color="#4d7a34"/>
        <stop offset="1" stop-color="#2c4a1f"/>
      </radialGradient>
    </defs>
    <rect width="548" height="764" fill="url(#burlap-cover)"/>
    <rect width="548" height="240" fill="url(#paper)"/>
    <path d="M0,170 C170,110 360,160 548,110 L548,520 L0,520 Z" fill="var(--lime)"/>
    <path d="M0,186 C170,126 360,176 548,126 L548,520 L0,520 Z" fill="var(--teal)"/>
    <path d="M0,202 C170,142 360,192 548,142 L548,520 L0,520 Z" fill="var(--teal-soft)"/>
    <path d="M0,216 C170,156 360,206 548,156 L548,520 L0,520 Z" fill="url(#forest)" role="img" aria-label="Photo of a misty green forest path"/>
    <path d="M0,510 C200,545 390,470 548,440 L548,764 L0,764 Z" fill="var(--teal-soft)"/>
    <path d="M0,518 C200,553 390,478 548,448 L548,764 L0,764 Z" fill="#fff"/>
    <path d="M0,524 C200,559 390,484 548,454 L548,764 L0,764 Z" fill="var(--teal)"/>
    <path d="M0,542 C200,577 390,502 548,472 L548,764 L0,764 Z" fill="var(--lime)"/>
    <path d="M0,552 C200,587 390,512 548,482 L548,764 L0,764 Z" fill="url(#burlap-cover)"/>
  </svg>

  <div class="brand">
    <div class="brand__name">WILLOW CREST</div>
    <div class="brand__sub">ESTATE</div>
  </div>

  <h1 class="welcome">WELL COME</h1>
  <div class="gold-banner gold-banner--community">The Willow Crest Estate Community</div>

  <footer class="footer"><span>Charleston, S.C.</span><span>lowcountry-estates.example</span></footer>
</section>

<section class="page page--inside">
  <svg class="page__art" viewBox="0 0 548 764" width="548" height="764" aria-hidden="true">
    <defs>
      <linearGradient id="burlap-inside" x1="0" y1="0" x2="0" y2="1">
        <stop offset="0" stop-color="var(--burlap-light)"/>
        <stop offset="1" stop-color="var(--burlap-dark)"/>
      </linearGradient>
      <linearGradient id="oak-fade" x1="0" y1="0" x2="0" y2="1">
        <stop offset="0" stop-color="#e9e4d8" stop-opacity="0"/>
        <stop offset="0.3" stop-color="#e7e4da" stop-opacity="0.75"/>
        <stop offset="1" stop-color="#8c9278" stop-opacity="0.9"/>
      </linearGradient>
    </defs>
    <rect width="548" height="764" fill="url(#burlap-inside)"/>
    <rect x="0" y="470" width="548" height="240" fill="url(#oak-fade)" role="img" aria-label="Faded photo of a sprawling live oak tree"/>
    <rect width="548" height="200" fill="#fff"/>
    <path d="M0,182 C200,170 400,192 548,178 L548,255 C400,270 200,240 0,266 Z" fill="var(--teal)"/>
    <path d="M0,204 C200,192 400,214 548,200 L548,255 C400,270 200,240 0,266 Z" fill="#fff"/>
    <path d="M0,212 C200,200 400,222 548,208 L548,255 C400,270 200,240 0,266 Z" fill="var(--lime)"/>
    <path d="M0,230 C200,218 400,240 548,226 L548,255 C400,270 200,240 0,266 Z" fill="var(--teal-soft)"/>
  </svg>

  <div class="gold-banner gold-banner--about">About us</div>

  <div class="copy copy--intro">
    <p>Nestled on pristine Marley Isle, the Willow Crest Estate Community is a truly enviable locale. An unspoiled maritime forest and the island's meandering coastline create a stunning natural backdrop while proximity to Charleston's world-class dining and superior shops means that you never have to sacrifice comfort or style. Within the community, eighteen large, private home sites offer ample space to gather in an intimate setting with family and friends while the forty acre common area provides space for large gatherings and community events. Private pools, equestrian activities, racquet sports, and golfing are among the many community-based amenities that will connect you to your neighbors. Whether you seek a peaceful escape for deep relaxation, to adopt the spirit of Southern hospitality, or to immerse yourself in the Lowcountry experience Willow Crest is the perfect haven.</p>
  </div>

  <div class="gold-banner gold-banner--legend">The Legend of the Willow Crest</div>
  <div class="gold-banner gold-banner--outdoor">Embrace Outdoor Living and<br>Connect with Nature</div>

  <div class="copy copy--legend">
    <p>The community is named for South Carolina's enchanting Willow Crest Tree, a centuries-old live oak located at the heart of Marley Isle. Although the exact age of the Willow Crest is unknown, estimates based on the tree's size and condition suggest that the coastal oak is between 700 and 1500 years old. The tree predates recorded history on the island and likely stood its ground long before the arrival of Captain Aldous Fenn to the Americas. The ancient tree's massive, sprawling branches reach outward in all directions, covering more than 17,000 square feet of ground with its majestic shade. Standing more than 65 feet tall, the massive oak towers over the park that bears its name. This imposing beauty has become one of the area's most iconic natural wonders, drawing thousands of visitors each year. Situated amid a treasure trove of historic structures and man-made beauty, the park offers visitors a reminder of Mother Nature's strength, vitality, and splendor.</p>
  </div>

  <div class="copy copy--outdoor">
    <p>Life is better when lived outdoors and in the Lowcountry, nature beckons. Wake each morning to breathtaking sunrises and allow the warm, salt-kissed air to rejuvenate your soul. Spend your days enjoying one of the area's exquisite beaches or visit some of Charleston's inspiring heritage sites. During the early evenings, enjoy dinner alfresco before retiring on the veranda with family and friends. Gather around an outdoor fireplace to share the day's memories and create even more under the stars. Featuring both community and private docks, Willow Crest is a maritime paradise. Board your vessel to explore the tidal Ashwick River separating Marley Isle from the mainland or follow the Intracoastal Waterway to the sea. For the adventurous, a kayak or canoe is an ideal means for exploring the intricacies of the island's elaborate coastal marshes. Sport fishers will be pleased to find the channels teeming with flounder, cobia, mackerel, tarpon, white shrimp, and blue crabs. Non-anglers will also appreciate the plentiful array of aquatic life and availability of fresh daily seafood.</p>
  </div>

  <div class="copy copy--inland">
    <p>Inland, Charleston County is home to stunning city gardens, immaculate local parks, and quaint nature trails. Terrestrial wildlife is plentiful on the island and even a short hike is likely to yield amazing photo opportunities. The island is heavily populated by South Carolina's state animal, the white tailed deer, which can be seen bounding through the wooded terrain year-round. Wild turkeys, gray fox, flying squirrels, raccoon, bobcats, and bear also call the island home. For bird watchers, a close eye on the skies will yield handsome rewards. Heron, osprey, bald eagles, red-tailed hawks egrets, and wood storks all call the island home. Dozens of migratory species provide increased variety to an already impressive host of island regulars and are always a welcome herald to the changing seasons.</p>
    <p>Despite seeing an influx of visitors and new residents, a strong commitment to ecologically conscious growth promises that this natural wonderland will remain intact for generations to come. Coastal management, wildlife conservation, and the protection of the area's natural resources are paramount among the considerations and development is conducted responsibly and respectfully.</p>
  </div>

  <footer class="footer"><span>Charleston, S.C.</span><span>lowcountry-estates.example</span></footer>
</section>

</body>
</html>
```